Finding the Steadfast Female Athlete

I am making an athlete version of the book cover that you created before. I need a few modifications to the book, to differentiate the covers. I am not sure what I am looking for, but I would want some fom of "Athlete Version" of this book to differentiate from the parent addition I created before.

Target Market(s)

Female Athletes between 14-22, Parents of Female Athletes 12-22

Font styles to use
Sans Serif

Requirements
Must have
• The same vibe as the previous book cover. I need some differentiation, but keeping the same theme

```html
<!DOCTYPE html>
<html lang="en">
<head>
<meta charset="utf-8">
<title>Finding the Steadfast Female Athlete — Athlete Edition Cover</title>
<link rel="stylesheet" href="https://fonts.googleapis.com/css2?family=Bebas+Neue&family=Oswald:wght@400;600&family=Montserrat:wght@300;700;800&family=Arimo:wght@400;700&display=swap">
<style>
:root{
  --stage:#3a3a3a;
  --ink:#0e0e0e;
  --white:#ffffff;
  --text:#e6e6e6;
  --grey-title:#cfcfcf;
  --gold-light:#e4c97f;
  --gold:#c2a155;
  --gold-dark:#8a7036;
}
*{margin:0;padding:0;box-sizing:border-box}
html,body{width:1200px;height:1001px;overflow:hidden;background:var(--stage)}
.cover{position:absolute;left:39px;top:95px;width:1122px;height:810px;background:var(--ink);overflow:hidden}
.layer{position:absolute;overflow:visible}

/* back cover */
.back{position:absolute;left:0;top:0;width:526px;height:810px;background:linear-gradient(180deg,#0b0b0b,#151515)}
.blurb{position:absolute;left:40px;top:199px;width:462px;font-family:"Arimo",sans-serif;font-size:12.8px;line-height:14.5px;color:var(--text);text-align:justify}
.blurb p{margin-bottom:14.5px}
.blurb strong{color:var(--white);font-weight:700}
.about-rule{position:absolute;left:50px;top:390px;width:444px;height:18px;display:flex;align-items:center;gap:10px}
.about-rule .line{flex:1;height:1.5px;background:var(--gold)}
.about-rule .label{font-family:"Arimo",sans-serif;font-weight:700;font-size:15px;color:var(--gold)}
.author-photo{position:absolute;left:40px;top:422px;width:128px;height:128px;background:radial-gradient(circle at 50% 42%,#5c4c44,#1d1b1a 70%)}
.bio{position:absolute;left:46px;top:414px;width:455px;font-family:"Arimo",sans-serif;font-size:12.8px;line-height:16px;color:var(--text);text-align:justify}
.bio .photo-space{float:left;width:130px;height:144px}
.bio p{margin-bottom:16px}
.imprint{position:absolute;left:29px;top:693px;width:140px;text-align:center}
.imprint .ring{width:52px;height:52px;border-radius:50%;border:2px solid var(--gold);margin:0 auto 6px}
.imprint .name{font-family:"Montserrat",sans-serif;font-weight:800;font-size:12px;letter-spacing:1px;color:var(--white)}
.imprint .sub{font-family:"Montserrat",sans-serif;font-weight:800;font-size:7px;letter-spacing:1.5px;color:var(--white);margin-top:2px}

/* spine */
.spine{position:absolute;left:526px;top:0;width:67px;height:810px;background:linear-gradient(90deg,#101010,#181818,#101010)}
.spine-ring{position:absolute;left:17px;top:376px;width:38px;height:38px;border-radius:50%;border:2px solid var(--gold)}

/* front cover */
.front{position:absolute;left:593px;top:0;width:529px;height:810px;background:#121212}
.front-photo{position:absolute;left:0;top:0;width:529px;height:810px;
  background:radial-gradient(ellipse 46% 50% at 47% 40%,#dcdcdc 0%,#a5a5a5 28%,#555 58%,rgba(18,18,18,0) 100%)}

.t-kicker{font-family:"Oswald",sans-serif;font-weight:600;fill:var(--white)}
.t-gold{font-family:"Bebas Neue",sans-serif}
.t-sub-title{font-family:"Oswald",sans-serif;font-weight:400;fill:var(--grey-title)}
.t-spine{font-family:"Bebas Neue",sans-serif;fill:var(--white)}
.t-spine .accent{fill:var(--gold)}
.t-name{font-family:"Montserrat",sans-serif;font-weight:700;fill:var(--white)}
.t-tag{font-family:"Montserrat",sans-serif;font-weight:300;fill:var(--white)}
</style>
</head>
<body>
<div class="cover">

  <section class="back">
    <svg class="layer" style="left:130px;top:20px" width="290" height="175" viewBox="0 0 290 175" aria-label="Finding the Steadfast Female Athlete">
      <defs>
        <linearGradient id="goldBack" x1="0" y1="0" x2="0" y2="1">
          <stop offset="0" stop-color="#e4c97f"/><stop offset=".5" stop-color="#c2a155"/><stop offset="1" stop-color="#8a7036"/>
        </linearGradient>
      </defs>
      <text class="t-kicker" x="41" y="26" font-size="25" textLength="200" lengthAdjust="spacing">FINDING THE</text>
      <text class="t-gold" x="8" y="145" font-size="160" textLength="267" lengthAdjust="spacingAndGlyphs" fill="url(#goldBack)">STEADFAST</text>
      <text class="t-kicker" x="43" y="167" font-size="25" textLength="198" lengthAdjust="spacing">FEMALE ATHLETE</text>
    </svg>

    <div class="blurb">
      <p><strong>Finding the Steadfast Female Athlete</strong> is more than a book about training; it’s a call to action for athletes, coaches, and anyone who wants to see girls rise strong in sport and in life.</p>
      <p>Grounded in years of coaching experience and real conversations with athletes and parents, this book delivers practical, no-fluff guidance on what young female athletes truly need: smart nutrition, intentional recovery, habits of success, and a mindset that holds strong under pressure.</p>
      <p>Whether you’re stepping onto the field for the first time or chasing down scholarships, this book equips you to train well, compete with purpose, and grow through every stage of your journey. Because being STEADFAST isn’t just how you play, it’s about who you become.</p>
    </div>

    <div class="about-rule"><span class="line"></span><span class="label">About the author</span><span class="line"></span></div>
    <div class="author-photo" role="img" aria-label="Portrait photograph of the author"></div>
    <div class="bio">
      <div class="photo-space"></div>
      <p>Daniel Marsh, CSCS, is the owner of Motion Strength Studio in Elmwood, Ohio, where he’s spent the last decade helping over 1,000 female athletes maximize performance, minimize injury risk, and build steadfast confidence.</p>
      <p>A former collegiate athlete turned performance coach, Daniel’s passion for training female athletes began after working with a young soccer player recovering from ACL surgery a moment that transformed his career and ignited a mission to change the way girls are trained and developed.</p>
      <p>Daniel believes every girl deserves the confidence to know she’s capable, strong, and created with purpose. He is also an author and speaker, presenting to schools and companies, as well as at the Peak Motion Training Summit, where he shares his expertise in developing strong, resilient female athletes.</p>
    </div>

    <div class="imprint">
      <div class="ring"></div>
      <div class="name">STEADFAST</div>
      <div class="sub">— FEMALE ATHLETE —</div>
    </div>
  </section>

  <section class="spine">
    <svg class="layer" style="left:0;top:0" width="67" height="810" viewBox="0 0 67 810">
      <text class="t-spine" transform="translate(35,33) rotate(90)" x="0" y="0" dominant-baseline="central" font-size="20" textLength="272" lengthAdjust="spacing">FINDING THE <tspan class="accent">STEADFAST</tspan> FEMALE ATHLETE</text>
      <text class="t-name" transform="translate(36,529) rotate(90)" x="0" y="0" dominant-baseline="central" font-size="18" textLength="228" lengthAdjust="spacing">DANIEL MARSH</text>
    </svg>
    <div class="spine-ring"></div>
  </section>

  <section class="front">
    <div class="front-photo" role="img" aria-label="Black and white photo of a female athlete seen from behind in a burst of white chalk powder"></div>
    <svg class="layer" style="left:0;top:0" width="529" height="810" viewBox="0 0 529 810" aria-label="Finding the Steadfast Female Athlete, athlete blueprint, Daniel Marsh">
      <defs>
        <linearGradient id="goldFront" x1="0" y1="0" x2="0" y2="1">
          <stop offset="0" stop-color="#e4c97f"/><stop offset=".5" stop-color="#c2a155"/><stop offset="1" stop-color="#8a7036"/>
        </linearGradient>
      </defs>
      <text class="t-kicker" x="97" y="373" font-size="40" textLength="306" lengthAdjust="spacing">FINDING THE</text>
      <text class="t-gold" x="52" y="551" font-size="240" textLength="397" lengthAdjust="spacingAndGlyphs" fill="url(#goldFront)">STEADFAST</text>
      <text class="t-sub-title" x="102" y="589" font-size="34" textLength="302" lengthAdjust="spacing">FEMALE ATHLETE</text>

      <rect x="148" y="621" width="88" height="16" rx="8" fill="none" stroke="#ffffff" stroke-width="1"/>
      <text class="t-tag" x="107" y="634" font-size="13" textLength="34" lengthAdjust="spacing">THE</text>
      <text class="t-tag" x="192" y="634" font-size="13" text-anchor="middle" textLength="74" lengthAdjust="spacing">ATHLETE</text>
      <text class="t-tag" x="242" y="634" font-size="13" textLength="155" lengthAdjust="spacing">BLUEPRINT FOR</text>
      <text class="t-tag" x="256" y="650" font-size="13" text-anchor="middle" textLength="307" lengthAdjust="spacing">BECOMING STRONG, CONFIDENT,</text>
      <text class="t-tag" x="256" y="666" font-size="13" text-anchor="middle" textLength="322" lengthAdjust="spacing">AND MENTALLY TOUGH GIRLS IN</text>
      <text class="t-tag" x="256" y="682" font-size="13" text-anchor="middle" textLength="178" lengthAdjust="spacing">SPORTS AND LIFE</text>

      <text class="t-name" x="81" y="756" font-size="25" textLength="353" lengthAdjust="spacing">DANIEL MARSH</text>
    </svg>
  </section>

</div>
</body>
</html>
```